Velmora Harbor Church Direct Mail Postcard

We are launching a new church in Olathe Kansas (Kansas City suburb). People here are well educated and pretty affluent. There are many young families which is our mail target demo. We need a 6 inch by 11 inch postcard that will be for a mass mailer that will coincide with our launch. The goal is simply to get people to come to the church launch which is September 18th. We think the theme should be "What in Heaven are you here for?" or "God is not Mad at you..No Matter What?" or "The truth is...you matter." It needs to include a map to our church which is inside Copper Ridge Middle School: 18400 W 93rd St, Olathe, KS 66047. Service is at 10:00 am, Safe childcare is provided from infants up to 12 year olds. There should be some space for us to put in some messaging and bullets. Possibly include a few pictures of happy families and people worshiping. I’ve attached our Logo, but we actually need to flip the colors so that the blue arrow is on top and pointing down, and the gray arrow is pointing up.

Target Market(s)

Young Families

Industry/Entity Type

Church

Requirements
Must have
• Post Card should be front and back full color
• Our website clearly shown on the back: VelmoraHarborChurch.com
• There should be a small map on the back with our location.
• It should say our service starts at 10:00 and that we our first service is Sept 18th
• The message or images on the front are there primarily to get people to turn the card over. UPDATE: We like the idea "What in Heaven are you here for?" on the front the best, followed by "God is NOT Mad at you..." (front) "no matter what" (back) second, and then "The truth is.." (front) "You matter" back third.
• Only 1 of the themes should be used at a time. So for example, the front should say, "What In Heaven are you here for?" or "God is not mad at you..." but not both.
• We like clean, modern looks. Don't put the logo on the front.
Nice to have
• Some stock photos of families or people worshipping (contemporary charismatic church)
• I attached some examples of cards that worked well for other churches. Please check them out.
Should not have
• The words "Grand Opening"

```html
<!DOCTYPE html>
<html lang="en">
<head>
<meta charset="utf-8">
<title>Velmora Harbor Church Postcard</title>
<link rel="stylesheet" href="https://fonts.googleapis.com/css2?family=Libre+Baskerville:wght@700&family=Fira+Sans+Condensed:wght@400;600;700&family=Fira+Sans:wght@300;400;600;700&display=swap">
<style>
  :root{
    --stage:#a9ad9f;
    --panel:#dddcd6;
    --ink:#222222;
    --ink-soft:#3a3a3a;
    --blue:#1f3fe0;
    --rule:#3b4fd0;
    --paper:#ffffff;
    --headline:#2a1b1b;
  }
  *{box-sizing:border-box;margin:0;padding:0}
  html,body{width:1200px;height:1199px;overflow:hidden}
  body{background:var(--stage);position:relative;font-family:"Fira Sans",sans-serif;color:var(--ink)}

  .card{position:absolute;top:145px;width:507px;height:912px;overflow:hidden;box-shadow:0 6px 22px rgba(0,0,0,.25)}
  .card-front{left:78px}
  .card-back{left:619px;background:var(--panel)}

  .front-photo{position:absolute;inset:0;
    background:linear-gradient(180deg,#ece6df 0%,#d9cbbd 25%,#b99c88 50%,#7c5a55 68%,#3f2d36 78%,#2b2230 100%)}
  .front-headline{position:absolute;left:0;right:0;top:155px;text-align:center;
    font-family:"Libre Baskerville",serif;font-weight:700;font-size:49px;line-height:53px;color:var(--headline);letter-spacing:-.5px}

  .photo-strip{position:absolute;top:0;left:0;right:0;height:105px;display:flex}
  .photo{height:100%}
  .photo-1{width:166px;background:linear-gradient(135deg,#caa98a,#5d4a3e)}
  .photo-2{width:172px;background:linear-gradient(135deg,#8fae6a,#d8b8a0)}
  .photo-3{width:169px;background:linear-gradient(135deg,#e4ddd2,#8c7c70)}

  .abs{position:absolute;left:0;right:0;text-align:center}
  .kicker{top:130px;font-family:"Fira Sans Condensed",sans-serif;font-weight:700;font-size:17px}
  .church-name{top:158px;font-family:"Fira Sans Condensed",sans-serif;font-weight:700;font-size:35px;color:var(--blue);letter-spacing:-.3px;display:flex;justify-content:center;align-items:center;gap:10px}
  .church-name .mark{width:26px;height:26px;background:var(--blue)}
  .tagline{top:194px;font-weight:300;font-size:18px;color:var(--ink-soft)}
  .divider{position:absolute;top:231px;left:42px;width:415px;height:2px;background:var(--rule)}
  .opens{top:248px;font-size:25px;letter-spacing:1px;font-weight:400}
  .opens b{font-weight:700;letter-spacing:2px}
  .slash{color:var(--blue);font-style:italic}
  .service{top:283px;font-size:18px;font-weight:700;letter-spacing:.5px}
  .service .time{font-size:25px}
  .service small{font-size:14px}
  .pitch{top:322px;font-family:"Fira Sans Condensed",sans-serif;font-weight:700;font-size:14.5px;line-height:17px}
  .invite{top:366px;font-family:"Fira Sans Condensed",sans-serif;font-weight:600;font-size:14.5px}
  .about{top:397px;left:42px;right:42px;text-align:left;font-family:"Fira Sans Condensed",sans-serif;font-size:12.8px;line-height:16px}
  .find{position:absolute;top:462px;left:42px;right:50px;display:flex;align-items:center;gap:18px;font-family:"Fira Sans Condensed",sans-serif;font-weight:600;font-size:13px}
  .find::before,.find::after{content:"";flex:1;height:1px;background:var(--ink-soft)}
  .features{position:absolute;top:488px;left:42px;display:grid;grid-template-columns:185px 240px;row-gap:5px;list-style:none;font-family:"Fira Sans Condensed",sans-serif;font-weight:600;font-size:12.5px}
  .features li::before{content:"✓";color:var(--blue);margin-right:7px}
  .childcare{top:542px;font-family:"Fira Sans Condensed",sans-serif;font-weight:700;font-size:14px}
  .childcare .blue{color:var(--blue)}

  .mail-area{position:absolute;left:0;top:573px;width:263px;height:339px;background:var(--paper)}
  .map{position:absolute;left:274px;top:573px;width:200px;height:137px;background:#e6e6ea;border:2px solid #4a5bc8}
  .address{position:absolute;left:276px;top:718px;font-family:"Fira Sans Condensed",sans-serif;font-size:12.5px;line-height:14px}
  .address strong{font-weight:600}
  .website{position:absolute;left:275px;top:758px;font-family:"Fira Sans Condensed",sans-serif;font-weight:700;font-size:16px;color:var(--blue)}
  .stamp{position:absolute;left:359px;top:802px;width:115px;height:76px;border:1.5px dashed #8a8a8a}
</style>
</head>
<body>
  <section class="card card-front">
    <div class="front-photo" role="img" aria-label="Person walking alone along a bridge toward a cloudy sky with white doves"></div>
    <h1 class="front-headline">What in Heaven<br>are you here for?</h1>
  </section>

  <section class="card card-back">
    <div class="photo-strip">
      <div class="photo photo-1" role="img" aria-label="Smiling young couple embracing"></div>
      <div class="photo photo-2" role="img" aria-label="Two happy young girls cheek to cheek"></div>
      <div class="photo photo-3" role="img" aria-label="Smiling family with a young daughter"></div>
    </div>

    <p class="abs kicker">FIND THE ANSWERS AT</p>
    <p class="abs church-name"><span class="mark"></span>VELMORA HARBOR CHURCH</p>
    <p class="abs tagline">Love · Wisdom · Power</p>
    <div class="divider"></div>

    <p class="abs opens"><span class="slash">//</span>OPENS AT <b>SEPTEMBER18TH</b></p>
    <p class="abs service"><span class="slash">//</span> SERVICE STARTS AT <span class="time">10:00</span><small>AM</small></p>
    <p class="abs pitch">DON’T JUST SURVIVE, LIVE. LIVE TO THE FULLEST OF YOUR<br>HABILITIES, SHOUT TO THE HEAVENS WITH YOUR FULL VOICE.</p>
    <p class="abs invite">Bring your family and Join us on our first session.</p>
    <p class="abs about">At Velmora Harbor Church, we provide all the counseling you need to find a new path in life. We work to maintain the ultimate values of life, like love, wisdom and the commitment to help others.</p>

    <p class="find">At Velmora Harbor Church, you will find:</p>
    <ul class="features">
      <li>A friendly enviroment</li>
      <li>Enlightening messages and counseling</li>
      <li>Dinamic Worship Experience</li>
      <li>A safe enviroment for your children</li>
    </ul>
    <p class="abs childcare"><span class="blue">♥ SAFE CHILDCARE</span> FROM INFANTS UP TO 12 YEAR OLDS</p>

    <div class="mail-area"></div>
    <div class="map" role="img" aria-label="Street map showing Velmora Harbor Church inside Copper Ridge Middle School"></div>
    <p class="address"><strong>COPPER RIDGE MIDDLE SCHOOL</strong><br>18400 W 93RD ST, OLATHE, KS 66047</p>
    <p class="website">VelmoraHarborChurch.com</p>
    <div class="stamp"></div>
  </section>
</body>
</html>
```